DEAN COLLOPY PROPERTY SERVICES

I want a business card that is clean and simple.
'Dean Collopy Property Services' is the title.
Somewhere on the card needs to be 'Carpentry, Tiling, painting and garden services'

On the back of card
PH 087 394 1526
email: deancollopypropertyservices@fernmail.net

I have attached a picture of my other business. I would like the font and design to be similar to the bathroom business.

Many thanks.

```html
<!DOCTYPE html>
<html lang="en">
<head>
<meta charset="utf-8">
<title>Dean Collopy Property Services – Business Card</title>
<link rel="stylesheet" href="https://fonts.googleapis.com/css2?family=Montserrat:wght@500;600&family=Roboto:ital,wght@0,400;1,400&display=swap">
<style>
  :root {
    --backdrop: #2b2b2b;
    --card-dark: #1c1c1c;
    --card-light: #ececec;
    --ink-dark: #1a1a1a;
    --ink-light: #eeeeee;
    --band: #34383b;
    --band-edge: #43474a;
    --muted: #dcdcdc;
  }
  * { margin: 0; padding: 0; box-sizing: border-box; }
  html, body { width: 1200px; height: 1138px; overflow: hidden; }
  body { background: var(--backdrop); position: relative; font-family: "Roboto", sans-serif; }

  .card {
    position: absolute;
    width: 620px;
    height: 374px;
    border-radius: 16px;
    overflow: hidden;
  }
  .card--front { left: 274px; top: 186px; background: var(--card-dark); color: var(--ink-light); }
  .card--back  { left: 276px; top: 608px; background: var(--card-light); color: var(--ink-dark); }

  .wordmark { position: absolute; text-align: center; }
  .wordmark__name {
    font-family: "Montserrat", sans-serif;
    font-weight: 500;
    line-height: 1;
    white-space: nowrap;
  }
  .wordmark__tag {
    font-family: "Montserrat", sans-serif;
    font-weight: 600;
    letter-spacing: 0.36em;
    white-space: nowrap;
  }

  .card--front .wordmark { left: 0; right: 0; top: 150px; }
  .card--front .wordmark__name { font-size: 60px; }
  .card--front .wordmark__tag { font-size: 18px; margin-top: 8px; margin-right: -0.36em; }

  .services { font-size: 17px; letter-spacing: 0.01em; white-space: nowrap; }
  .services span { margin: 0 8px; }
  .card--front .services { position: absolute; left: 0; right: 0; top: 260px; text-align: center; color: var(--muted); }

  .card--back .wordmark { right: 38px; top: 84px; text-align: right; }
  .card--back .wordmark__name { font-size: 44px; font-weight: 600; }
  .card--back .wordmark__tag { font-size: 15px; margin-top: 6px; margin-right: -0.36em; }

  .holder { position: absolute; left: 44px; top: 200px; display: flex; align-items: baseline; gap: 12px; }
  .holder__name { font-family: "Montserrat", sans-serif; font-weight: 600; font-size: 24px; }
  .holder__role { font-style: italic; font-size: 14px; }

  .contact-band {
    position: absolute; left: 0; right: 0; top: 244px; bottom: 0;
    background: linear-gradient(180deg, var(--band-edge), var(--band));
    color: var(--ink-light);
    padding: 24px 0 0 44px;
  }
  .contact-line { display: flex; align-items: center; gap: 10px; font-size: 17px; height: 24px; }
  .contact-line svg { width: 19px; height: 19px; flex: none; }
  .contact-band .services { margin-top: 14px; margin-left: 0; }
  .contact-band .services span:first-child { margin-left: 0; }
</style>
</head>
<body>

<section class="card card--front" aria-label="Card front">
  <div class="wordmark">
    <div class="wordmark__name">Dean Collopy</div>
    <div class="wordmark__tag">PROPERTY SERVICES</div>
  </div>
  <p class="services">Carpentry<span>|</span>Tiling<span>|</span>Painting<span>|</span>Garden Services</p>
</section>

<section class="card card--back" aria-label="Card back">
  <div class="wordmark">
    <div class="wordmark__name">Dean Collopy</div>
    <div class="wordmark__tag">PROPERTY SERVICES</div>
  </div>

  <div class="holder">
    <span class="holder__name">Dean Collopy</span>
    <span class="holder__role">Owner &amp; Director</span>
  </div>

  <div class="contact-band">
    <div class="contact-line">
      <svg viewBox="0 0 20 20" aria-hidden="true">
        <circle cx="10" cy="10" r="9" fill="none" stroke="currentColor" stroke-width="1.4"/>
        <path d="M7 5.5l1.6 2.2-1 1.2c.6 1.3 1.6 2.3 2.9 2.9l1.2-1 2.2 1.6-.8 1.8c-3.6-.3-6.6-3.3-6.9-6.9z" fill="currentColor"/>
      </svg>
      <span>087 394 1526</span>
    </div>
    <div class="contact-line">
      <svg viewBox="0 0 20 20" aria-hidden="true">
        <circle cx="10" cy="10" r="9" fill="none" stroke="currentColor" stroke-width="1.4"/>
        <rect x="5" y="6.5" width="10" height="7" fill="none" stroke="currentColor" stroke-width="1.3"/>
        <path d="M5 6.5l5 4 5-4" fill="none" stroke="currentColor" stroke-width="1.3"/>
      </svg>
      <span>deancollopypropertyservices@fernmail.net</span>
    </div>
    <p class="services"><span>Carpentry</span><span>|</span>Tiling<span>|</span>Painting<span>|</span>Garden Services</p>
  </div>
</section>

</body>
</html>
```